Washington DC Solo Practitioner Law Firm needs Stationery and Business Card Design

We need a letterhead and business card for a new law firm based in Washington DC called Marlowe PLLC. The law firm is a single lawyer practicing appellate law (U.S. Supreme Court, Federal District Courts, State Supreme Courts).
We already have a logo designed through a PixelBazaar contest. The letterhead and the business card should include the Logo and have the same look and feel as the Logo - same fonts and colors, please. We would like a clean, crisp, simple, professional look. The design should convey stability and experience.
We have .png and .psd and .ai files for the logo, as needed
Dark blue color is PANTONE P 108-16 C
Grey color is PANTONE P 179-11 C
Type face is Century Gothic Regular typeface

```html
<!DOCTYPE html>
<html lang="en">
<head>
<meta charset="utf-8">
<title>Marlowe PLLC – Business Card</title>
<link href="https://fonts.googleapis.com/css2?family=Didact+Gothic&family=Montserrat:wght@700&display=swap" rel="stylesheet">
<style>
  :root {
    --navy: #003a63;
    --grey: #8a8d91;
    --text: #3d4247;
    --paper: #ffffff;
    --backdrop: #e9e9ec;
  }
  html, body {
    margin: 0;
    width: 1200px;
    height: 934px;
    overflow: hidden;
    background: var(--backdrop);
    font-family: "Didact Gothic", "Century Gothic", sans-serif;
  }
  .canvas {
    position: relative;
    width: 1200px;
    height: 934px;
  }
  .card {
    position: absolute;
    width: 520px;
    height: 297px;
    box-shadow: 0 6px 18px rgba(0, 0, 0, 0.12);
    overflow: hidden;
  }
  /* Reverse side */
  .card--back {
    left: 100px;
    top: 130px;
    background: var(--navy);
  }
  .card--back .brand {
    position: absolute;
    left: 0;
    right: 0;
    top: 112px;
    display: flex;
    flex-direction: column;
    align-items: center;
    color: #ffffff;
  }
  .card--back .brand-row {
    display: flex;
    align-items: center;
    gap: 14px;
  }
  .brand-square {
    width: 22px;
    height: 22px;
    background: currentColor;
  }
  .brand-name {
    font-size: 30px;
    letter-spacing: 2px;
    line-height: 1;
  }
  .brand-tagline {
    margin-top: 10px;
    font-size: 9.5px;
    letter-spacing: 0.8px;
  }
  /* Front side */
  .card--front {
    left: 580px;
    top: 500px;
    background: var(--paper);
  }
  .card--front .brand {
    position: absolute;
    right: 36px;
    top: 40px;
    display: flex;
    flex-direction: column;
    align-items: flex-end;
    color: var(--navy);
  }
  .card--front .brand-row {
    display: flex;
    align-items: center;
    gap: 12px;
  }
  .card--front .brand-name { font-size: 26px; }
  .card--front .brand-tagline {
    margin-top: 8px;
    font-size: 8.5px;
    color: var(--grey);
  }
  .contact {
    position: absolute;
    right: 36px;
    top: 128px;
    text-align: right;
    font-size: 12px;
    line-height: 17px;
    color: var(--text);
  }
  .contact .address { margin-bottom: 12px; }
  .contact .label {
    color: var(--navy);
    font-weight: bold;
  }
  .holder-name {
    position: absolute;
    left: 32px;
    bottom: 52px;
    margin: 0;
    font-family: "Montserrat", "Century Gothic", sans-serif;
    font-weight: 700;
    font-size: 19px;
    letter-spacing: 0.5px;
    color: var(--navy);
  }
  .footer-band {
    position: absolute;
    left: 0;
    right: 0;
    bottom: 0;
    height: 20px;
    background: var(--navy);
  }
</style>
</head>
<body>
<main class="canvas">
  <section class="card card--back" aria-label="Business card, reverse side">
    <div class="brand">
      <div class="brand-row">
        <span class="brand-square"></span>
        <span class="brand-name">MARLOWE PLLC</span>
      </div>
      <span class="brand-tagline">TRIAL AND APPELLATE LITIGATION</span>
    </div>
  </section>

  <section class="card card--front" aria-label="Business card, front side">
    <div class="brand">
      <div class="brand-row">
        <span class="brand-square"></span>
        <span class="brand-name">MARLOWE PLLC</span>
      </div>
      <span class="brand-tagline">TRIAL AND APPELLATE LITIGATION</span>
    </div>
    <div class="contact">
      <div class="address">
        1840 L Street NW, Suite 410<br>
        Washington, DC 20036
      </div>
      <div><span class="label">T:</span> 202-555-0148 · <span class="label">F:</span> 571-555-0193</div>
      <div><span class="label">E:</span> gmarlowe@marlowepllc.com</div>
    </div>
    <h1 class="holder-name">GRANT MARLOWE</h1>
    <div class="footer-band"></div>
  </section>
</main>
</body>
</html>
```